Monument sign* - Law Firm

*I am installing a monument sign that has LED, as well as backlit elements. I am seeking help in designing the backlit portion of the sign. The Backlit sign will be 12’ x 4’.

We are looking for a classic, yet eye-catching sign to help new and current clients find our firm as well as bring in future clients. One of our goals is that people who drive by on a regular basis remember our sign (and us) for any future legal need.

Target Market(s)

Current and future clientele

Industry/Entity Type

Law Firm

Font styles to use
Serif
Sans Serif

Colors
b1b1b1
333333

Requirements
Must have
• Business name: Hargrove Law Firm, Inc.
• Website: www.hargrovelawfirm-example.com
• Telephone: (555)214-3679
• Our firm's logo
Nice to have
• Color preference is black, taupe, and white. A photo for reference of the office coloring is uploaded.
• We currently have an established logo which our firm has been using for more than 10 years. Our logo has been used in advertising, commercials, letterhead, and on-site. We are looking to transition from brown/rust/cream to the black/taupe/white color scheme.
Should not have
• Cheesy slogans; character designs; directions; additional symbols outside of the firm's logo.

```html
<!DOCTYPE html>
<html lang="en">
<head>
<meta charset="utf-8">
<title>Hargrove Law Firm, Inc. — Monument Sign</title>
<link href="https://fonts.googleapis.com/css2?family=Cinzel:wght@400;700&display=swap" rel="stylesheet">
<style>
  :root {
    --taupe: #8f8478;
    --black: #050505;
    --white: #ffffff;
    --ink: #1a1a1a;
    --line: #d9d4ce;
  }
  html, body {
    margin: 0;
    padding: 0;
    width: 1200px;
    height: 401px;
    overflow: hidden;
    background: var(--white);
  }
  .sign {
    display: block;
    width: 1200px;
    height: 401px;
  }
  .band-taupe { fill: var(--taupe); }
  .field-black { fill: var(--black); }
  .logo-plate { fill: var(--white); }
  .band-rule { fill: var(--line); }
  .logo-square { fill: var(--taupe); }
  .logo-name {
    font-family: "Cinzel", serif;
    font-weight: 700;
    font-size: 24px;
    fill: var(--ink);
    letter-spacing: 1px;
  }
  .website {
    font-family: "Cinzel", serif;
    font-weight: 700;
    font-size: 22px;
    fill: var(--white);
    letter-spacing: 1px;
  }
  .phone {
    font-family: "Cinzel", serif;
    font-weight: 400;
    font-size: 21px;
    fill: var(--white);
    letter-spacing: 1px;
  }
  .firm-name {
    font-family: "Cinzel", serif;
    font-weight: 700;
    font-size: 64px;
    fill: var(--white);
  }
</style>
</head>
<body>
<svg class="sign" viewBox="0 0 1200 401" xmlns="http://www.w3.org/2000/svg">
  <!-- taupe band, split around the logo plate -->
  <path class="band-taupe" d="M0 98 H132 Q155 98 155 121 V152 H0 Z"/>
  <path class="band-taupe" d="M392 152 V121 Q392 98 415 98 H1200 V152 Z"/>

  <!-- thin rule under the band -->
  <rect class="band-rule" x="0" y="152" width="1200" height="1"/>

  <!-- black field -->
  <rect class="field-black" x="0" y="153" width="1200" height="248"/>

  <!-- logo plate -->
  <path class="logo-plate" d="M155 0 H392 V226 Q392 250 368 250 H179 Q155 250 155 226 Z"/>
  <rect class="logo-square" x="210" y="30" width="120" height="120"/>
  <text class="logo-name" x="273.5" y="200" text-anchor="middle">HARGROVE</text>

  <!-- contact details -->
  <text class="website" x="1157" y="135" text-anchor="end">WWW.HARGROVELAWFIRM-EXAMPLE.COM</text>
  <text class="phone" x="1155" y="192" text-anchor="end">Tel : (555) 214 3679</text>

  <!-- firm name -->
  <text class="firm-name" x="71" y="357" textLength="1082" lengthAdjust="spacingAndGlyphs">HARGROVE LAW FIRM, INC.</text>
</svg>
</body>
</html>
```